Mobile Accessory Business - Brightfern - Needs Retail Packaging!

**ECO Design is not working we need to change it**

We need retail packaging designed for mobile phone accessories. This includes; mobile phone screen protectors, mobile phone cases and mobile phone cables.

We want the packaging to be simplistic, vibrant modern and minimalist.

Example:

https://www.findora-example.com.au/imgres?imgurl=https%3A%2F%2Fcdn.pixvault-example.net%2Fattachments%2Fattachment_10482761&imgrefurl=http%3A%2F%2Fcraftpitch-example.com%2Fpackaging%2Fcontests%2Fscreen-protector-packaging-551207

The packaging for each product should create a clear brand across the products i.e if a customer comes into a shop and picks up a mobile phone case they know from looking at the box's which mobile phone screen protector or mobile phone cable is ours.

We are a new company that does not provide cheap "tradly" accessories. We provide luxury accessories at a premium price.

We need a package designed for each of the following:

1) Mobile Phone Screen Protectors - The packaging needs to be standard hang cell size (for the mobile phone industry). The dimensions of the packaging should be: 18cm (H) X 10.5cm (W) and include a hanging hook. The thickness should be similar to the thickness of an envelope. This does not need a window for viewing the product as its a simple screen protector (which is essentially a clear sheet of contact).

Features: 9H (hardness), Completely flexible, they are not actually glass (made up of a nano technology, call it Lumo Plate, Hydrophobic (keeps fingerprints off), 99% transparent, does not smash like glass.

2) Mobile Phone Cases - The packaging needs to be standard hang cell size (for the mobile phone industry). The dimensions of the packaging should be: 18cm (H) X 10.5cm (W) X 2cm (D) and include a hanging hook. The product should have a viewing window so the entire contents can be see. The product should be easily and readily removed without causing damage to the contents or the packaging.

E.g (only more vibrant) https://www.findora-example.com.au/search?q=mobile+phone+case+packaging&tbm=isch#q=phone+case+packaging&imgrc=Qx7PlmRtaVwZdK%3A

Features: Whilst we will be selling several types of cases start with a design for leather cases, 100% genuine lather (first layer cow hide), TPU insert instead of hard plastic for more protection, 3 card slots,

3) Mobile Phone Cables (USB etc) - The packaging needs to be standard hang cell size (for the mobile phone industry). The dimensions of the packaging should be: 18cm (H) X 5cm (W) X 2cm (D) and include a hanging hook. The product should have a viewing window so the entire contents can be see.

E.g. (only with a viewing window) https://www.findora-example.com.au/search?q=mobile+phone+case+packaging&tbm=isch#q=micro%20usb%20packaging&imgrc=Hb3WqnTzLe8kYp%3A

Features: Braided (for strength), reversible (doesn't matter which way you plug it in), 2m in length.

The packaging for the cases needs to be accessible so customers can open it and view the case. Finally we need a window on the packaging so the product can be viewed (cable and cases)

Target Market(s)

The target market is very broad. Everyone from teenagers to the middle age purchase mobile phone accessories.

At our core is 14 --> 45 males and females.

These accessories are primarily sold in Corvana (and alike) shops in rural area's of Australia.

Industry/Entity Type

Telecommunications

Font styles to use
Serif
Sans Serif

Colors
0292cd
6b449b
00a990
9bcb3c

Requirements
Must have
• Designs for the three products mentioned in the description.
• We want the packaging to be simplistic, vibrant modern and minimalist
• Placeholders on the front for USP's.
• ******************************************************
• What needs to be on screen protectors
• FRONT
• Logo
• Heading
• (1) Scratch Resistant
• (2) Impact Resistant
• Sub-Heading
• (1) Screen Protector
• Unique Selling Points
• Space for 5 unique selling points
• BACK
• Logo
• Product Description
• Space for 6 lines
• Replacement Warranty
• 2 Year replacement warranty image/if you break it we replace it
• Barcode
• Space big enough for barcode to be stuck on
• Email Address
• This is an example of what would be written on the back of the case packaging
• "Brightfern accessories is an Australian
• owned company providing high quality
• products. We know how important it is
• for your device to be protected, so now
• your device has its own brightfern made
• from the highest quality leather and
• hand stitched to perfection."
• Contact Details:
• Email: sales@brightfernaccessories.com.au
• Barcode:
• We need a place to put a sticker with a barcode on the back of each set of packaging barcode will be the same size for each box.
• Warranty:
• Screen Protectors - 2 Year replacement warranty, If they break the screen protector We will replace it.
• Cases: 2 Year warranty
• Cables: 2 Year warranty

```html
<!DOCTYPE html>
<html lang="en">
<head>
<meta charset="utf-8">
<title>Brightfern – Mobile Phone Cases Packaging</title>
<link href="https://fonts.googleapis.com/css2?family=Montserrat:wght@300;400;700&family=Open+Sans:wght@300;400;600;700&family=Ubuntu:wght@500;700&display=swap" rel="stylesheet">
<style>
  :root{
    --bg:#eeeeee;
    --green-deep:#0e5a1c;
    --green-mid:#2f8f25;
    --green-bright:#57b533;
    --lime:#9bcb3c;
    --black:#121212;
    --white:#ffffff;
    --gold:#d99a2b;
    --gold-deep:#a8631a;
    --window-fill:#d9f6c2;
    --phone:#8ee84a;
  }
  *{box-sizing:border-box;margin:0;padding:0}
  html,body{width:1200px;height:1200px;overflow:hidden}
  body{background:radial-gradient(circle at 50% 45%,#fafafa 0%,var(--bg) 70%,#dcdcdc 100%);font-family:"Open Sans",sans-serif;position:relative}

  .panel{position:absolute;top:110px;width:460px;height:980px;overflow:hidden}
  .panel--front{left:90px}
  .panel--back{left:650px}

  .hang-tab{position:absolute;left:0;top:0;width:100%;height:110px;background:linear-gradient(90deg,var(--green-mid) 0%,#5fae2e 60%,var(--lime) 100%)}
  .hang-slot{position:absolute;top:46px;left:50%;width:86px;height:18px;margin-left:-43px;background:var(--white);border-radius:9px}

  /* front */
  .front-body{position:absolute;top:110px;left:0;width:100%;height:770px;
    background:linear-gradient(180deg,#1c1c1c 0%,var(--black) 42%,#1d4f17 52%,var(--green-mid) 62%,var(--green-deep) 100%)}
  .logo{font-family:"Montserrat",sans-serif;font-weight:400;color:var(--white);letter-spacing:-1px;line-height:1}
  .front-body .logo{position:absolute;top:70px;left:170px;font-size:54px}
  .window{position:absolute;top:180px;left:130px;width:300px;height:580px;border:8px solid #eef7ea;border-radius:34px;background:var(--window-fill);box-shadow:0 0 10px rgba(0,0,0,.35)}
  .phone{position:absolute;inset:18px 18px 22px 14px;border-radius:26px;background:linear-gradient(160deg,#a6f26a 0%,var(--phone) 45%,#6fd532 100%)}
  .side-title{position:absolute;left:38px;top:760px;transform:rotate(-90deg);transform-origin:0 0;white-space:nowrap;display:flex;align-items:center;gap:14px}
  .side-title__main{font-family:"Montserrat",sans-serif;font-size:38px;font-weight:300;color:var(--white);letter-spacing:1px}
  .side-title__main b{font-weight:700}
  .side-title__tag{position:absolute;left:330px;top:-46px;background:var(--black);color:var(--white);font-size:19px;padding:2px 12px;border-radius:8px;border:1px solid #444}
  .seal{position:absolute;border-radius:50%;background:radial-gradient(circle,#f3c259 0%,var(--gold) 55%,var(--gold-deep) 100%);box-shadow:0 0 0 5px #c37d22,0 3px 6px rgba(0,0,0,.35)}
  .front-body .seal{left:370px;top:660px;width:96px;height:96px}
  .footer-band{position:absolute;left:0;bottom:0;width:100%;height:100px;background:linear-gradient(90deg,#0c4d17,var(--green-deep));border-top:2px solid rgba(255,255,255,.5)}
  .email{font-family:"Ubuntu",sans-serif;font-weight:700;color:var(--white);font-size:21px;letter-spacing:.5px;text-align:center;line-height:100px}

  /* back */
  .back-body{position:absolute;top:110px;left:0;width:100%;height:870px;
    background:radial-gradient(ellipse at 80% 40%,#6bc63a 0%,var(--green-bright) 25%,var(--green-mid) 55%,var(--green-deep) 100%)}
  .back-body .logo{position:absolute;top:90px;left:36px;font-size:58px}
  .back-body .seal{left:330px;top:50px;width:100px;height:100px}
  .heading{position:absolute;top:180px;left:36px;font-family:"Montserrat",sans-serif;font-size:28px;font-weight:300;color:var(--white)}
  .heading b{font-weight:700}
  .tag{position:absolute;top:222px;left:36px;background:var(--black);color:var(--white);font-size:14px;padding:1px 7px;border-radius:5px}
  .about{position:absolute;top:260px;left:34px;width:390px;font-size:16.5px;font-weight:300;line-height:24px;color:var(--white)}
  .features{position:absolute;top:430px;left:36px;width:190px;color:var(--white)}
  .features h3{font-size:17px;font-weight:700;margin-bottom:4px}
  .features ul{list-style:none}
  .features li{font-size:16px;font-weight:300;line-height:24px;padding-left:14px;position:relative}
  .features li::before{content:"";position:absolute;left:0;top:8px;width:8px;height:8px;border-radius:50%;background:var(--black)}
  .divider{position:absolute;top:420px;left:232px;width:1px;height:180px;background:rgba(255,255,255,.45)}
  .warranty{position:absolute;top:420px;left:252px;width:160px;height:180px}
  .barcode-space{position:absolute;top:660px;left:100px;width:260px;height:150px;background:var(--white);border:2px solid #cfcfcf;display:flex;align-items:center;justify-content:center;font-family:"Ubuntu",sans-serif;font-weight:500;font-size:20px;color:#222}
  .contact{position:absolute;top:835px;left:0;width:100%;text-align:center;font-size:20px;font-weight:300;color:var(--white)}
  .back-footer{position:absolute;left:0;bottom:0;width:100%;height:80px;border-top:2px solid rgba(255,255,255,.5);background:linear-gradient(90deg,#0c4d17,var(--green-deep))}
  .back-footer .email{line-height:78px}
</style>
</head>
<body>

<section class="panel panel--front" aria-label="Front of pack">
  <div class="hang-tab"><div class="hang-slot"></div></div>
  <div class="front-body">
    <div class="logo">Brightfern</div>
    <div class="window">
      <div class="phone" role="img" aria-label="Bright green phone in a clear case seen through the viewing window"></div>
    </div>
    <div class="side-title">
      <span class="side-title__main">MOBILE PHONE <b>CASES</b></span>
      <span class="side-title__tag">Leather Cases</span>
    </div>
    <div class="seal" aria-label="Quality seal"></div>
  </div>
  <div class="footer-band"><div class="email">sales@brightfernaccessories.com.au</div></div>
</section>

<section class="panel panel--back" aria-label="Back of pack">
  <div class="hang-tab"><div class="hang-slot"></div></div>
  <div class="back-body">
    <div class="logo">Brightfern</div>
    <div class="seal" aria-label="Quality seal"></div>
    <h2 class="heading">MOBILE PHONE <b>CASES</b></h2>
    <span class="tag">Leather Cases</span>
    <p class="about">Brightfern accessories is an Australian owned company providing high quality products. We know how important it is for your device to be protected, so now your device has its own brightfern made from the highest quality leather and hand stitched to perfection.</p>
    <div class="features">
      <h3>Features:</h3>
      <ul>
        <li>Leather Cases</li>
        <li>100% Genuine Lather</li>
        <li>TPU insert instead of hard plastic for more protection</li>
        <li>3 card slots</li>
      </ul>
    </div>
    <div class="divider"></div>
    <svg class="warranty" viewBox="0 0 160 180" aria-label="2 year warranty">
      <defs><path id="warranty-arc" d="M20,110 A62,62 0 0 1 140,70"/></defs>
      <text font-family="Montserrat, sans-serif" font-weight="700" font-size="20" fill="#fff" letter-spacing="2"><textPath href="#warranty-arc">WARRANTY</textPath></text>
      <circle cx="90" cy="118" r="54" fill="#1a1a1a" stroke="#d8d8d8" stroke-width="3"/>
      <text x="90" y="130" text-anchor="middle" font-family="Montserrat, sans-serif" font-weight="700" font-size="46" fill="#fff">2</text>
      <text x="90" y="156" text-anchor="middle" font-family="Montserrat, sans-serif" font-weight="700" font-size="22" fill="#ddd">YEAR</text>
    </svg>
    <div class="barcode-space">Barcode</div>
    <div class="contact">Contact Details:</div>
  </div>
  <div class="back-footer"><div class="email">sales@brightfernaccessories.com.au</div></div>
</section>

</body>
</html>
```